Brivol Partner Process pdf

Design a professional sales document in PDF format for Brivol.com, showcasing our services and value to potential prospects.

```html
<!DOCTYPE html>
<html lang="en">
<head>
<meta charset="utf-8">
<title>Brivol Partner Process</title>
<link rel="stylesheet" href="https://fonts.googleapis.com/css2?family=Poppins:wght@300;400;500;600;700;800&display=swap">
<style>
:root{
  --bg:#a3a3a3;
  --paper:#ffffff;
  --blue:#4471b8;
  --blue-deep:#2f5ea8;
  --yellow:#fdd062;
  --gold:#e9b531;
  --ink:#1a1a1a;
  --muted:#333333;
}
*{margin:0;padding:0;box-sizing:border-box}
html,body{width:1200px;height:1200px;overflow:hidden;background:var(--bg);font-family:"Poppins",sans-serif;color:var(--ink)}
.page{position:absolute;top:248px;width:528px;height:684px;background:var(--paper);box-shadow:0 2px 10px rgba(0,0,0,.18);overflow:hidden}
.page--front{left:58px}
.page--back{left:621px}
.abs{position:absolute}

/* front */
.brand-top{left:0;right:0;top:30px;text-align:center;font-size:40px;font-weight:700;color:var(--blue);letter-spacing:-.5px}
.hero{left:0;top:95px;width:528px;height:268px}
.partner-with{left:0;right:0;top:386px;text-align:center;font-size:25px;font-weight:400;letter-spacing:3px}
.headline-name{left:0;right:0;top:408px;text-align:center;font-size:72px;font-weight:700;color:var(--blue);line-height:1;letter-spacing:-2px}
.tagline-main{left:0;right:0;top:474px;text-align:center;font-size:33px;font-weight:600;line-height:1.1}
.promise-pill{left:65px;width:398px;top:523px;height:28px;border-radius:14px;background:var(--blue);color:#fff;font-size:17px;text-align:center;line-height:29px}
.intro{left:110px;width:308px;top:562px;text-align:center;font-size:10.4px;line-height:12.4px;color:var(--ink)}
.rule{top:635px;height:1px;background:#222;width:100px}
.rule--l{left:58px}.rule--r{left:370px}
.web-pill{left:166px;width:195px;top:624px;height:22px;border-radius:11px;background:var(--yellow);text-align:center;line-height:23px;font-size:14px;letter-spacing:1.5px}
.web-pill b{font-weight:600}

/* back */
.steps-title{left:0;right:0;top:24px;text-align:center;font-size:18.5px;font-weight:700}
.steps-title .five{display:inline-block;width:20px;height:22px;border:2px solid var(--blue);color:var(--blue);line-height:18px;text-align:center;font-size:19px;vertical-align:-2px;margin:0 2px}
.steps-title .accent{color:var(--blue)}
.step-rail{left:67px;top:96px;width:1px;height:266px;background:var(--blue)}
.step-badge{width:56px;height:56px;left:40px}
.step-badge span{position:absolute;left:0;right:0;text-align:center;font-weight:700;color:var(--ink)}
.step-badge .lbl{top:17px;font-size:7px;font-weight:500}
.step-badge .num{top:22px;font-size:15px}
.step{left:113px;width:270px}
.step h3{font-size:10.3px;font-weight:700;color:var(--blue);line-height:12px;margin-bottom:5px;letter-spacing:.1px}
.step ul{list-style:none}
.step li{position:relative;padding-left:8px;font-size:7.6px;line-height:9.4px;color:var(--ink)}
.step li::before{content:"";position:absolute;left:0;top:3px;width:4px;height:4px;border:1.2px solid var(--blue);border-radius:50%}
.step li.gap{margin-top:3px}
.step-photo{left:385px;width:98px;border-radius:5px}

.why-band{left:0;top:449px;width:528px;height:235px;background:var(--blue)}
.why-tab{left:157px;top:440px;width:214px;height:26px}
.why-tab span{position:absolute;left:0;right:0;top:4px;text-align:center;font-size:14px;font-weight:700}
.perk{width:160px}
.perk h4{position:relative;padding-left:9px;font-size:10.2px;font-weight:700;color:var(--yellow);line-height:12px}
.perk h4::before{content:"";position:absolute;left:0;top:4px;width:4px;height:4px;border:1.2px solid var(--yellow);border-radius:50%}
.perk p{padding-left:9px;font-size:7.8px;line-height:9.5px;color:#fff;margin-top:1px}
.perk--l{left:43px}.perk--r{left:311px;width:190px}
.seal{left:214px;top:510px;width:88px;height:88px}
.join{left:316px;top:566px;color:#fff}
.join h5{font-size:14.5px;font-weight:700;line-height:16px}
.join h5 span{font-weight:400}
.join p{font-size:8.2px;font-weight:600;line-height:10.3px;margin-top:3px}
.call-label{left:45px;top:617px;font-size:7.6px;font-weight:700;color:#fff}
.call-label span{color:var(--yellow)}
.contact{top:630px;color:#fff;font-weight:600;display:flex;align-items:center;gap:4px}
.contact--phone{left:45px;font-size:11.5px}
.contact--mail{left:160px;font-size:8.3px;top:633px}
.brand-foot{left:290px;top:627px;font-size:17px;font-weight:700;color:var(--yellow);line-height:20px}
.foot-web{left:376px;top:629px;width:115px;height:14px;border-radius:7px;background:var(--yellow);font-size:8px;letter-spacing:.8px;text-align:center;line-height:14.5px;color:var(--ink)}
</style>
</head>
<body>

<section class="page page--front">
  <div class="abs brand-top">Brivol</div>

  <svg class="abs hero" viewBox="0 0 528 268">
    <defs>
      <linearGradient id="movers" x1="0" y1="0" x2="1" y2="1">
        <stop offset="0" stop-color="#7b7a5c"/>
        <stop offset=".5" stop-color="#b9b3a3"/>
        <stop offset="1" stop-color="#6d6a60"/>
      </linearGradient>
    </defs>
    <rect x="0" y="0" width="43" height="268" fill="#c79e2c" role="img" aria-label="Warm-tinted strip of the moving scene"/>
    <rect x="49" y="0" width="340" height="268" fill="url(#movers)" role="img" aria-label="Two movers loading wrapped furniture and boxes into a van"/>
    <polygon points="386,0 528,0 528,268 386,268 502,134" fill="var(--blue-deep)" role="img" aria-label="Van interior with stacked boxes, blue tinted"/>
    <polygon points="386,0 400,0 508,134 400,268 386,268 502,134" fill="var(--yellow)"/>
    <polyline points="372,0 488,134 372,268" fill="none" stroke="#fff" stroke-width="3"/>
  </svg>

  <div class="abs partner-with">Partner with</div>
  <div class="abs headline-name">Brivol</div>
  <div class="abs tagline-main">The Un-Van Line</div>
  <div class="abs promise-pill">Close More Deals. Earn More. Work Smarter</div>
  <p class="abs intro">Brivol empowers independent movers with instant guaranteed pricing, unlimited commission potential, and a logistics-driven approach that eliminates the risks of long-haul moves.</p>
  <div class="abs rule rule--l"></div>
  <div class="abs rule rule--r"></div>
  <div class="abs web-pill">www.<b>brivol</b>.com</div>
</section>

<section class="page page--back">
  <h2 class="abs steps-title">HOW IT WORKS <span class="five">5</span> <span class="accent">SIMPLE STEPS</span></h2>

  <div class="abs step-rail"></div>
  <svg class="abs step-badge" style="top:68px" viewBox="0 0 56 56"><rect x="11" y="11" width="34" height="34" transform="rotate(45 28 28)" fill="#fff" stroke="var(--blue)" stroke-width="1.6" rx="3"/><rect x="15" y="15" width="26" height="26" transform="rotate(45 28 28)" fill="var(--yellow)" rx="2"/><text x="28" y="23" text-anchor="middle" font-family="Poppins,sans-serif" font-size="7">STEP</text><text x="28" y="38" text-anchor="middle" font-family="Poppins,sans-serif" font-size="15" font-weight="700">1</text></svg>
  <svg class="abs step-badge" style="top:135px" viewBox="0 0 56 56"><rect x="11" y="11" width="34" height="34" transform="rotate(45 28 28)" fill="#fff" stroke="var(--blue)" stroke-width="1.6" rx="3"/><rect x="15" y="15" width="26" height="26" transform="rotate(45 28 28)" fill="var(--yellow)" rx="2"/><text x="28" y="23" text-anchor="middle" font-family="Poppins,sans-serif" font-size="7">STEP</text><text x="28" y="38" text-anchor="middle" font-family="Poppins,sans-serif" font-size="15" font-weight="700">2</text></svg>
  <svg class="abs step-badge" style="top:202px" viewBox="0 0 56 56"><rect x="11" y="11" width="34" height="34" transform="rotate(45 28 28)" fill="#fff" stroke="var(--blue)" stroke-width="1.6" rx="3"/><rect x="15" y="15" width="26" height="26" transform="rotate(45 28 28)" fill="var(--yellow)" rx="2"/><text x="28" y="23" text-anchor="middle" font-family="Poppins,sans-serif" font-size="7">STEP</text><text x="28" y="38" text-anchor="middle" font-family="Poppins,sans-serif" font-size="15" font-weight="700">3</text></svg>
  <svg class="abs step-badge" style="top:272px" viewBox="0 0 56 56"><rect x="11" y="11" width="34" height="34" transform="rotate(45 28 28)" fill="#fff" stroke="var(--blue)" stroke-width="1.6" rx="3"/><rect x="15" y="15" width="26" height="26" transform="rotate(45 28 28)" fill="var(--yellow)" rx="2"/><text x="28" y="23" text-anchor="middle" font-family="Poppins,sans-serif" font-size="7">STEP</text><text x="28" y="38" text-anchor="middle" font-family="Poppins,sans-serif" font-size="15" font-weight="700">4</text></svg>
  <svg class="abs step-badge" style="top:334px" viewBox="0 0 56 56"><rect x="11" y="11" width="34" height="34" transform="rotate(45 28 28)" fill="#fff" stroke="var(--blue)" stroke-width="1.6" rx="3"/><rect x="15" y="15" width="26" height="26" transform="rotate(45 28 28)" fill="var(--yellow)" rx="2"/><text x="28" y="23" text-anchor="middle" font-family="Poppins,sans-serif" font-size="7">STEP</text><text x="28" y="38" text-anchor="middle" font-family="Poppins,sans-serif" font-size="15" font-weight="700">5</text></svg>

  <div class="abs step" style="top:67px">
    <h3>IDENTIFY A BRIVOL OPPORTUNITY</h3>
    <ul>
      <li>Interstate moves (300+ miles)</li>
      <li>Shipment size: 1,000 lbs to over 20,000 lbs</li>
      <li>Customer needs a professional, full-service moving solution</li>
      <li>If it's a fit, move to pricing</li>
    </ul>
  </div>
  <div class="abs step" style="top:134px">
    <h3>LOG IN &amp; GET AN INSTANT GUARANTEED PRICE</h3>
    <ul>
      <li>Log in to the Brivol Partner Portal</li>
      <li>Enter customer move details into our AI-powered pricing tool</li>
      <li>Get a wholesale price quote in seconds</li>
    </ul>
  </div>
  <div class="abs step" style="top:201px">
    <h3>CUSTOMIZE YOUR PROFIT</h3>
    <ul>
      <li>Set your own earnings by marking up the wholesale price</li>
      <li><b>Suggested markup: 10–20%</b> (capped for larger shipments)</li>
      <li>You control how much you earn per move</li>
    </ul>
  </div>
  <div class="abs step" style="top:271px">
    <h3>BOOK THE MOVE &amp; COLLECT YOUR COMMISSION</h3>
    <ul>
      <li>Book the move instantly</li>
      <li>Collect the deposit upfront—this is typically your commission</li>
      <li>Brivol handles all logistics, scheduling, and support</li>
    </ul>
  </div>
  <div class="abs step" style="top:333px">
    <h3>STAY UPDATED &amp; KEEP CLOSING DEALS</h3>
    <ul>
      <li>Regular updates: Automated &amp; personal notifications<br>keep you in the loop</li>
      <li class="gap">Dedicated account manager: Always available for support</li>
      <li class="gap">Mentorship &amp; training: Learn best practices from<br>top-performing partners</li>
      <li class="gap">Ongoing optimization: Brivol constantly improves based<br>on feedback</li>
    </ul>
  </div>

  <div class="abs step-photo" style="top:63px;height:59px;background:linear-gradient(135deg,#e9e4dc,#b79a78)" role="img" aria-label="Couple among moving boxes checking a laptop"></div>
  <div class="abs step-photo" style="top:130px;height:59px;background:linear-gradient(180deg,#2f9be0 0 45%,#c9b08c 45%)" role="img" aria-label="Coin jars beside a blank easel board"></div>
  <div class="abs step-photo" style="top:195px;height:59px;background:linear-gradient(135deg,#dfe4ea,#9a7c5c)" role="img" aria-label="Stacks of coins growing in height"></div>
  <div class="abs step-photo" style="top:262px;height:59px;background:linear-gradient(135deg,#8a5a38,#d9cbb8)" role="img" aria-label="Handshake over a desk with laptop and papers"></div>
  <div class="abs step-photo" style="top:336px;height:58px;background:linear-gradient(135deg,#f2f0ee,#b9bcc2)" role="img" aria-label="Hands typing on a laptop sign-up page"></div>

  <div class="abs why-band"></div>
  <svg class="abs why-tab" viewBox="0 0 214 26"><polygon points="14,0 200,0 214,26 0,26" fill="var(--yellow)"/></svg>
  <div class="abs why-tab"><span>WHY BRIVOL?</span></div>

  <div class="abs perk perk--l" style="top:484px"><h4>INSTANT AUTHORITY</h4><p>Give customers a guaranteed price on the first call, doubling your close rate.</p></div>
  <div class="abs perk perk--l" style="top:523px"><h4>FULL CONTROL</h4><p>Set your own markup and maximize revenue without a cap.</p></div>
  <div class="abs perk perk--l" style="top:563px"><h4>ZERO LONG-HAUL HASSLE</h4><p>No truck commitments or operational headaches—Brivol handles everything.</p></div>

  <svg class="abs seal" viewBox="0 0 88 88">
    <polygon fill="var(--gold)" points="44,2 50,9 58,5 62,13 71,12 72,21 80,23 78,31 86,36 81,43 86,50 79,55 81,63 73,66 72,75 63,75 59,83 51,80 44,86 37,80 29,83 25,75 16,75 15,66 7,63 9,55 2,50 7,43 2,36 10,31 8,23 16,21 17,12 26,13 30,5 38,9"/>
    <circle cx="44" cy="44" r="32" fill="var(--yellow)"/>
    <g font-family="Poppins,sans-serif" font-weight="600" font-size="7.4" text-anchor="middle" fill="#1a1a1a">
      <text x="44" y="28">Move</text><text x="44" y="35">Smarter.</text>
      <text x="44" y="48">Move Better.</text>
      <text x="44" y="62">Move with</text><text x="44" y="69">Brivol</text>
    </g>
  </svg>

  <div class="abs perk perk--r" style="top:484px"><h4>AI-POWERED PRICING</h4><p>More accurate than any traditional van line, ensuring a seamless experience.</p></div>
  <div class="abs perk perk--r" style="top:523px"><h4>PREMIUM CUSTOMER EXPERIENCE</h4><p>Every move is handled by top-tier local crews at both origin &amp; destination.</p></div>
  <div class="abs join"><h5>JOIN BRIVOL <span>TODAY</span></h5><p>CONVERT MORE MOVES. EARN MORE.<br>WORK SMARTER.</p></div>

  <div class="abs call-label">SCHEDULE A <span>CALL NOW</span></div>
  <div class="abs contact contact--phone">
    <svg width="11" height="11" viewBox="0 0 24 24"><path fill="var(--yellow)" d="M6.6 10.8a15.1 15.1 0 0 0 6.6 6.6l2.2-2.2a1 1 0 0 1 1-.25 11.4 11.4 0 0 0 3.6.57 1 1 0 0 1 1 1V20a1 1 0 0 1-1 1A17 17 0 0 1 3 4a1 1 0 0 1 1-1h3.5a1 1 0 0 1 1 1c0 1.25.2 2.45.57 3.57a1 1 0 0 1-.25 1z"/></svg>
    (800) 555-0147
  </div>
  <div class="abs contact contact--mail">
    <svg width="10" height="8" viewBox="0 0 20 14"><rect x="1" y="1" width="18" height="12" fill="none" stroke="var(--yellow)" stroke-width="2"/><path d="M1 1l9 7 9-7" fill="none" stroke="var(--yellow)" stroke-width="2"/></svg>
    support@brivol.com
  </div>
  <div class="abs brand-foot">Brivol</div>
  <div class="abs foot-web">www.brivol.com</div>
</section>

</body>
</html>
```